Used Car Dealer seeks an Amazing Business Card Design

We are looking for a business card design that incorporates our logo and grabs the attention of anyone we give the business card to.

Looking to use the same colors as the logo. Our Logo choice is the black background with Red and Silver/Grey Lettering.

We also would like to see some embossed designs.

Target Market(s)

Used Car Buyers, Automotive, Auto

Industry/Entity Type

Automotive

Contact Information for Business Card

BVEL7K
Gordon Whitlock
482 Tarrow Lane
Suite 207
Denmore, GA 30412
Office (770) 555-0142
Cell (770) 555-0187
bvel7kga@quellmail.com
www.bvel7kga.com

Colors
ffffff
ee3036

Requirements
Must have
• Must include our logo (Black Background with Red and Silver/Grey Lettering)
Nice to have
• Embossed Design. Can be Single or Double Sided.

```html
<!DOCTYPE html>
<html lang="en">
<head>
<meta charset="utf-8">
<title>BVEL7K Business Card</title>
<link href="https://fonts.googleapis.com/css2?family=Exo+2:ital,wght@1,900&family=Open+Sans:wght@400;700&display=swap" rel="stylesheet">
<style>
  :root {
    --stage-top: #5b7e94;
    --stage-bottom: #2d4a5d;
    --card-black: #121212;
    --metal-dark: #1b1b1d;
    --metal-light: #2e2f31;
    --silver: #d6d8db;
    --text-white: #ffffff;
    --text-grey: #c9c9c9;
    --brand-red: #ee3036;
    --map-tone: #262626;
  }
  * { margin: 0; padding: 0; box-sizing: border-box; }
  html, body { width: 1200px; height: 675px; overflow: hidden; }
  body {
    background: linear-gradient(160deg, var(--stage-top), var(--stage-bottom));
    font-family: "Open Sans", Arial, sans-serif;
    position: relative;
  }
  .card {
    position: absolute;
    top: 190px;
    width: 520px;
    height: 297px;
    border-radius: 3px;
    overflow: hidden;
    box-shadow: 0 18px 30px rgba(0,0,0,0.45);
  }
  .card--front {
    left: 50px;
    background:
      repeating-linear-gradient(0deg, rgba(255,255,255,0.025) 0 1px, transparent 1px 3px),
      linear-gradient(135deg, var(--metal-light), var(--metal-dark) 55%, #232426);
  }
  .card--back {
    left: 630px;
    background: var(--card-black);
  }
  .brand {
    position: absolute;
    display: flex;
    align-items: center;
    gap: 12px;
  }
  .brand__dot {
    width: 26px; height: 26px;
    border-radius: 50%;
    background: var(--brand-red);
  }
  .brand__name {
    font-family: "Open Sans", Arial, sans-serif;
    font-weight: 700;
    color: var(--silver);
    letter-spacing: 1px;
  }
  .card--front .brand { left: 160px; top: 100px; }
  .card--front .brand__name { font-size: 46px; }
  .front__web {
    position: absolute;
    left: 0; right: 0; bottom: 42px;
    text-align: center;
    color: var(--text-grey);
    font-size: 14px;
    letter-spacing: 1.5px;
  }
  .front__web .accent { color: var(--brand-red); }
  .world-map {
    position: absolute;
    left: 150px; top: 20px;
    width: 350px; height: 250px;
    border-radius: 40%;
    background: radial-gradient(ellipse at center, var(--map-tone), transparent 70%);
  }
  .card--back .brand { left: 28px; top: 102px; }
  .card--back .brand__dot { width: 20px; height: 20px; }
  .card--back .brand__name { font-size: 34px; }
  .contact {
    position: absolute;
    left: 262px; top: 62px;
    color: var(--text-white);
  }
  .contact__name {
    font-family: "Exo 2", "Arial Black", sans-serif;
    font-weight: 900;
    font-style: italic;
    font-size: 22px;
    text-transform: uppercase;
    letter-spacing: 0.5px;
    margin-bottom: 10px;
  }
  .contact__name .surname { color: var(--brand-red); }
  .contact__company { font-weight: 700; font-size: 12px; }
  .contact__address { font-size: 12px; line-height: 1.45; margin-bottom: 6px; }
  .contact__list { list-style: none; font-size: 12.5px; }
  .contact__list li { display: flex; align-items: center; gap: 7px; height: 20px; }
  .contact__icon {
    width: 14px; height: 14px;
    border-radius: 50%;
    background: var(--text-white);
    display: flex; align-items: center; justify-content: center;
  }
  .contact__icon svg { width: 9px; height: 9px; }
</style>
</head>
<body>

  <section class="card card--front" aria-label="Business card front">
    <div class="brand">
      <span class="brand__dot"></span>
      <span class="brand__name">BVEL7K</span>
    </div>
    <p class="front__web">www.<span class="accent">bvel7kga</span>.com</p>
  </section>

  <section class="card card--back" aria-label="Business card back">
    <div class="world-map" role="img" aria-label="Faint dark world map backdrop"></div>
    <div class="brand">
      <span class="brand__dot"></span>
      <span class="brand__name">BVEL7K</span>
    </div>
    <div class="contact">
      <h1 class="contact__name">Gordon <span class="surname">Whitlock</span></h1>
      <p class="contact__company">BVEL7K</p>
      <p class="contact__address">482 Tarrow Lane, Suite 207<br>Denmore, GA 30412</p>
      <ul class="contact__list">
        <li>
          <span class="contact__icon"><svg viewBox="0 0 10 10"><path d="M2 1h2l1 2-1 1a5 5 0 0 0 2 2l1-1 2 1v2a1 1 0 0 1-1 1A7 7 0 0 1 1 2a1 1 0 0 1 1-1z" fill="#121212"/></svg></span>
          (770) 555-0142
        </li>
        <li>
          <span class="contact__icon"><svg viewBox="0 0 10 10"><rect x="3" y="0.5" width="4" height="9" rx="0.8" fill="#121212"/><rect x="3.7" y="1.5" width="2.6" height="5.5" fill="#fff"/></svg></span>
          (770) 555-0187
        </li>
        <li>
          <span class="contact__icon"><svg viewBox="0 0 10 10"><rect x="1" y="2.5" width="8" height="5" fill="#121212"/><path d="M1 2.5l4 3 4-3" stroke="#fff" stroke-width="0.7" fill="none"/></svg></span>
          bvel7kga@quellmail.com
        </li>
        <li>
          <span class="contact__icon"><svg viewBox="0 0 10 10"><circle cx="5" cy="5" r="4" fill="none" stroke="#121212" stroke-width="1"/><ellipse cx="5" cy="5" rx="1.8" ry="4" fill="none" stroke="#121212" stroke-width="0.8"/><path d="M1 5h8" stroke="#121212" stroke-width="0.8"/></svg></span>
          www.bvel7kga.com
        </li>
      </ul>
    </div>
  </section>

</body>
</html>
```